Tri-Fold Brochure for Transportation Equipment Dealer

We need a design of a new tri-fold brochure for our company. This is what we give to customers and prospective customers. Many of our customers do not know the diversity of our product line and capabilities. We have a lot of information to share with them in a small package. I have provided a draft of the content that I wanted included (in a .pptx and .pdf format), but we need it enhanced with color and made to look more professional. We need it to be informative yet professional.

Target Market(s)

Transportation industry customers. Fleet carriers and owner/operator truck drivers.

Industry/Entity Type

Truck Service

Font styles to use
Serif
Sans Serif

Colors
3176b5

Requirements
Must have
• Color. Must include the information that I have provided in the draft. Must be US Letter size.
Nice to have
• Color and separation of different sections.

```html
<!DOCTYPE html>
<html lang="en">
<head>
<meta charset="UTF-8">
<title>Dry Bulk Equipment Brochure Cover</title>
<link href="https://fonts.googleapis.com/css2?family=Saira+Condensed:wght@500;600;700&family=Open+Sans:wght@400;700&display=swap" rel="stylesheet">
<style>
  :root {
    --brand-blue: #1d5fa8;
    --brand-mid: #3176b5;
    --brand-navy: #0c2d52;
    --paper: #eeeff0;
    --paper-light: #fafafa;
    --ink: #2b2b2b;
    --rule: #3a3a3a;
    --stage: #d9dadc;
  }
  * { box-sizing: border-box; margin: 0; padding: 0; }
  html, body { width: 1200px; height: 1200px; overflow: hidden; }
  body { background: var(--stage); position: relative; font-family: "Open Sans", sans-serif; }

  .cover-panel {
    position: absolute; left: 340px; top: 40px; width: 520px; height: 1120px;
    background: linear-gradient(180deg, var(--paper-light) 0%, var(--paper) 55%, #e6e7e9 100%);
    overflow: hidden; box-shadow: 0 2px 10px rgba(0,0,0,.15);
  }

  .brand-mark {
    position: absolute; top: 110px; left: 0; width: 100%;
    text-align: center; color: var(--brand-blue);
    font-family: "Saira Condensed", sans-serif; font-weight: 700;
    font-size: 46px; letter-spacing: 1px; line-height: 1.05;
    text-transform: uppercase;
  }
  .brand-mark .brand-square {
    display: inline-block; width: 22px; height: 22px; background: var(--brand-blue);
    margin-right: 12px; vertical-align: 4px;
  }

  .company-names {
    position: absolute; top: 300px; left: 52px; list-style: none;
    font-family: "Saira Condensed", sans-serif; font-weight: 600;
    color: var(--brand-blue); font-size: 48px; line-height: 56px;
    text-transform: uppercase; letter-spacing: .5px;
  }

  .tagline-band {
    position: absolute; top: 492px; left: 0; width: 100%; height: 108px;
    background: var(--brand-blue); color: #fff; text-align: center;
    font-family: "Saira Condensed", sans-serif; font-weight: 600;
    text-transform: uppercase; font-size: 27px; line-height: 34px;
    padding-top: 20px;
  }
  .tagline-band .band-tail {
    position: absolute; right: 0; top: 0; width: 70px; height: 100%;
    background: var(--brand-navy); clip-path: polygon(40% 0, 100% 0, 100% 100%, 0 100%);
  }
  .tagline-band p { position: relative; }

  .product-grid {
    position: absolute; top: 612px; left: 34px; width: 452px; height: 368px;
    display: grid; grid-template-columns: 1fr 1fr; grid-template-rows: 1fr 1fr;
  }
  .product-grid::before {
    content: ""; position: absolute; left: 50%; top: 0; bottom: 0; width: 1.5px; background: var(--rule);
  }
  .product-cell { position: relative; padding: 8px 12px 0; border-bottom: 1.5px solid var(--rule); }
  .product-photo {
    height: 134px; border-radius: 4px;
    background: radial-gradient(ellipse at 50% 55%, #c9ccd1 0%, #9ea4ad 45%, rgba(230,231,233,0) 75%);
  }
  .product-label {
    font-weight: 700; font-size: 15px; color: var(--ink); margin-top: 10px;
  }

  .contact-block {
    position: absolute; top: 990px; right: 40px; text-align: left; z-index: 2;
  }
  .contact-phone {
    font-family: "Saira Condensed", sans-serif; font-weight: 700;
    font-size: 46px; line-height: 46px; color: var(--brand-blue); letter-spacing: .5px;
  }
  .contact-web { font-size: 17px; line-height: 22px; color: var(--ink); margin-top: 2px; }

  .footer-band {
    position: absolute; bottom: 0; left: 0; width: 100%; height: 40px; background: var(--brand-blue);
  }
  .footer-band .footer-wedge {
    position: absolute; right: 0; top: -16px; width: 190px; height: 56px;
    background: var(--brand-navy); clip-path: polygon(25% 0, 100% 0, 100% 100%, 0 100%, 0 30%);
  }
</style>
</head>
<body>
  <main class="cover-panel">
    <div class="brand-mark"><span class="brand-square"></span>Coastline<br>Pneumatic Group</div>

    <ul class="company-names">
      <li>Coastline Pneumatic</li>
      <li>Mesa Ridge Pneumatic</li>
      <li>Harborline Exports</li>
    </ul>

    <section class="tagline-band">
      <span class="band-tail"></span>
      <p>Experts in dry bulk transportation solutions</p>
      <p>New | Used | Services | Parts</p>
    </section>

    <section class="product-grid">
      <div class="product-cell">
        <div class="product-photo" role="img" aria-label="Photo of a pneumatic tank trailer"></div>
        <p class="product-label">Pneumatics</p>
      </div>
      <div class="product-cell">
        <div class="product-photo" role="img" aria-label="Photo of an end dump trailer"></div>
        <p class="product-label">End Dump</p>
      </div>
      <div class="product-cell">
        <div class="product-photo" role="img" aria-label="Photo of an electric blower unit"></div>
        <p class="product-label">Electric</p>
      </div>
      <div class="product-cell">
        <div class="product-photo" role="img" aria-label="Photo of a trailer-mounted diesel blower"></div>
        <p class="product-label">Diesel</p>
      </div>
    </section>

    <div class="contact-block">
      <p class="contact-phone">800-555-0142</p>
      <p class="contact-web">www.drybulkhaulers.com</p>
    </div>

    <div class="footer-band"><span class="footer-wedge"></span></div>
  </main>
</body>
</html>
```